Bref créative
Business Cards and Stationary for Conference App Company
Kalvornet
Modern
Lars Henrik Dalsgaard
Partner
Solbærvej 254
DK-2800 Kgs. Lyngby
lhd@kalvornet.example
kalvornet.example

```html
<!DOCTYPE html>
<html lang="en">
<head>
<meta charset="utf-8">
<title>Kalvornet — Business Card</title>
<link href="https://fonts.googleapis.com/css2?family=Open+Sans:wght@400;600;700&display=swap" rel="stylesheet">
<style>
  :root {
    --page-bg: #e9e7e4;
    --card-white: #ffffff;
    --band-grey: #8e9092;
    --accent-orange: #f39a1e;
    --logo-grey: #6a6c6e;
    --text-white: #ffffff;
  }
  * { margin: 0; padding: 0; box-sizing: border-box; }
  html, body {
    width: 1200px; height: 902px; overflow: hidden;
    background: var(--page-bg);
    font-family: "Open Sans", Arial, sans-serif;
  }
  .business-card {
    position: absolute; left: 100px; top: 165px;
    width: 1000px; height: 571px;
    background: var(--card-white);
    box-shadow: 0 10px 30px rgba(0,0,0,0.18);
    overflow: hidden;
  }
  .card-shapes { position: absolute; inset: 0; }
  .brand {
    position: absolute; left: 92px; top: 92px;
    display: flex; align-items: center; gap: 22px;
  }
  .brand-mark {
    width: 58px; height: 58px; background: var(--accent-orange);
  }
  .brand-name {
    font-size: 66px; font-weight: 400; color: var(--logo-grey);
    letter-spacing: -1px; line-height: 1;
  }
  .person {
    position: absolute; right: 130px; top: 292px; text-align: right;
    color: var(--text-white);
  }
  .person-name { font-size: 24px; font-weight: 700; }
  .person-role { font-size: 18px; font-weight: 400; margin-top: 2px; }
  .web-address {
    position: absolute; right: 42px; top: 500px;
    color: var(--text-white); font-size: 18px; font-weight: 600;
    letter-spacing: 4px;
  }
  .contact-list {
    position: absolute; left: 64px; top: 318px; list-style: none;
    color: var(--text-white); font-size: 20px; line-height: 1.25;
  }
  .contact-item { display: flex; align-items: flex-start; gap: 12px; margin-bottom: 6px; }
  .contact-icon {
    flex: none; width: 24px; height: 24px; border-radius: 50%;
    background: var(--text-white); margin-top: 1px;
    display: flex; align-items: center; justify-content: center;
  }
  .contact-icon svg { width: 14px; height: 14px; fill: var(--band-grey); }
</style>
</head>
<body>
  <div class="business-card">
    <svg class="card-shapes" viewBox="0 0 1000 571" width="1000" height="571">
      <rect class="lower-band" x="0" y="262" width="1000" height="309" fill="var(--band-grey)"/>
      <polygon class="name-pointer" points="690,262 730,262 700,288" fill="var(--accent-orange)"/>
      <path class="accent-wave" d="M0,548 L520,548 C600,548 620,478 700,478 L1000,478 L1000,571 L0,571 Z" fill="var(--accent-orange)"/>
    </svg>

    <div class="brand">
      <span class="brand-mark"></span>
      <span class="brand-name">Kalvornet</span>
    </div>

    <div class="person">
      <p class="person-name">Lars Henrik Dalsgaard</p>
      <p class="person-role">Partner</p>
    </div>

    <p class="web-address">www.kalvornet.example</p>

    <ul class="contact-list">
      <li class="contact-item">
        <span class="contact-icon"><svg viewBox="0 0 16 16"><path d="M8 1a5 5 0 0 0-5 5c0 4 5 9 5 9s5-5 5-9a5 5 0 0 0-5-5zm0 7a2 2 0 1 1 0-4 2 2 0 0 1 0 4z"/></svg></span>
        <span>Solbærvej 254<br>DK-2800 Kgs. Lyngby</span>
      </li>
      <li class="contact-item">
        <span class="contact-icon"><svg viewBox="0 0 16 16"><path d="M4 1l2.5 3-1.5 2c1 2 3 4 5 5l2-1.5 3 2.5-1.5 2.5C8 15 1 8 1.5 2.5z"/></svg></span>
        <span>45 61829073</span>
      </li>
      <li class="contact-item">
        <span class="contact-icon"><svg viewBox="0 0 16 16"><path d="M1 3h14v10H1zm1.5 1.5v.3L8 9l5.5-4.2v-.3z"/></svg></span>
        <span>lhd@kalvornet.example</span>
      </li>
      <li class="contact-item">
        <span class="contact-icon"><svg viewBox="0 0 16 16"><path d="M8 1a7 7 0 1 0 0 14A7 7 0 0 0 8 1zm0 1.6c.8 1 1.4 2.5 1.5 4.4h-3c.1-1.9.7-3.4 1.5-4.4zM2.7 9h2.3c.1 1.6.5 3 1.1 4a5.5 5.5 0 0 1-3.4-4zm0-2a5.5 5.5 0 0 1 3.4-4C5.5 4 5.1 5.4 5 7zm5.3 6.4c-.8-1-1.4-2.5-1.5-4.4h3c-.1 1.9-.7 3.4-1.5 4.4zM9.9 13c.6-1 1-2.4 1.1-4h2.3a5.5 5.5 0 0 1-3.4 4zM11 7c-.1-1.6-.5-3-1.1-4a5.5 5.5 0 0 1 3.4 4z"/></svg></span>
        <span>www.kalvornet.example</span>
      </li>
    </ul>
  </div>
</body>
</html>
```